Website for psychology clinic

We need a website for a psychology business by the name of "tranquil harbour psychology". Our psychology practice is based in Melbourne across 3 locations and provides psychological assessment, treatment and support (on an individual and group level) to clients experiencing a range of psychological issues including depression, anxiety, adjustment issues, relationship issues, and specifically eating disorders.
Most of our clients are relatively young with the majority of our clientele being women ranging from adolescence to middle-aged.

Target Market(s)

A range of clients from adolescents to older-aged adults seeking psychological support for issues including depression, anxiety, adjustment issues, and relationship issues. A number of our staff specialise in eating disorders and body image issues (predominantly females) and this makes up a large portion of our business. We would like to market ourselves toward individuals with disordered eating, however would like to encompass a broader range of issues such as those mentioned above.
General Practitioners (doctors) refer largely to our service and therefore would want this to be user friendly

Industry/Entity Type

Clinic

Font styles to use
Sans Serif
Script

Colors
9bcb3c
0455a3
ffffff
85cae6
cee9f5

Requirements
Must have
• Must include logo design (see attached logo) - tranquil harbour

Themes of personal growth, change and development as per my business name and logo - suggestive of a therapeutic journey
Nice to have
• A warm and inviting homepage with a welcoming message -

I really love the website brackenwellcare.co.uk and would love to use this as a guide as to what I would like.
Would like a simple yet elegant - not too wordy website page - something with enough information for the client
I also like the simplicity of clinicpagesnet.com.au and have attached a couple of examples in the images section. brackenwellcare.co.uk is my preference however.
I will add images that I would like to use, ideally I would like the use if quotation bubbles as used in this website
Nice to have the following pages -
HOME page
ABOUT
LOCATION
CONTACT US
GP INFORMATION
PATIENT INFORMATIOn
- include "a client form" page for the client to type their details directly into a form which sends directly to the psychologist
MAKE AN ENQUIRY
LINKS
Should not have
• Should not look too chaotic or crowded

```html
<!DOCTYPE html>
<html lang="en">
<head>
<meta charset="utf-8">
<title>Tranquil Harbour Psychology</title>
<link href="https://fonts.googleapis.com/css2?family=Lato:wght@400;700&family=Open+Sans:wght@400;600&display=swap" rel="stylesheet">
<style>
:root{
  --green:#7bb431;
  --brand-green:#9bcb3c;
  --blue:#0455a3;
  --sky:#85cae6;
  --ice:#cee9f5;
  --ink:#333;
  --muted:#666;
  --rule:#e3e3e3;
  --band:#f8f8f8;
  --foot:#232323;
  --foot-bar:#2b2b2b;
  --foot-text:#bbb;
}
*{box-sizing:border-box;margin:0;padding:0}
html,body{width:913px;height:1200px;overflow:hidden;background:#fff}
body{font-family:"Open Sans",Arial,sans-serif;color:var(--ink);position:relative}
.abs{position:absolute}
.site-header{position:absolute;left:0;top:0;width:913px;height:53px;border-bottom:1px solid var(--rule)}
.brand{position:absolute;left:152px;top:17px;display:flex;align-items:center;gap:6px;font-family:Lato,sans-serif;font-weight:700;font-size:15px;color:var(--blue)}
.brand .dot{width:9px;height:9px;border-radius:50%;background:var(--brand-green)}
.nav{position:absolute;top:21px;font-size:8.2px;color:#777}
.nav.active{color:#333;font-weight:600}
.nav-underline{position:absolute;left:410px;top:51px;width:39px;height:2px;background:var(--green)}
.title-band{position:absolute;left:0;top:54px;width:913px;height:34px;background:var(--band);border-bottom:1px solid var(--rule)}
.page-title{position:absolute;left:146px;top:10px;font-size:10.5px;color:#555}
.crumbs{position:absolute;left:707px;top:13px;font-size:6.8px;color:#555}
.hero{position:absolute;left:0;top:88px;width:913px;height:386px;border-bottom:1px solid var(--rule)}
.hero-photo{position:absolute;left:0;top:0;width:490px;height:386px;background:radial-gradient(ellipse at 45% 55%,#8cc55a 0%,#c7e2a8 30%,#f4ede6 60%,#fff 85%)}
.hero-title{position:absolute;left:498px;top:133px;font-family:Lato,sans-serif;font-size:36px;color:#333;letter-spacing:-.3px}
.hero-sub{position:absolute;left:502px;top:176px;font-family:Lato,sans-serif;font-size:14px;line-height:18.5px;color:var(--blue)}
.hero-brand{position:absolute;left:540px;top:261px;display:flex;align-items:center;gap:8px;font-family:Lato,sans-serif;font-weight:700;font-size:26px;color:var(--blue)}
.hero-brand .dot{width:14px;height:14px;border-radius:50%;background:var(--brand-green)}
.ctrl{position:absolute;top:366px;width:14px;height:14px;border-radius:50%}
h2.section{position:absolute;font-family:"Open Sans",sans-serif;font-weight:400;font-size:12.2px;color:#222;background:#fff;padding-right:10px}
.h-rule{position:absolute;height:1px;background:var(--rule)}
.body-copy{position:absolute;left:146px;top:529px;width:406px;font-size:7.75px;line-height:12.8px;color:#666}
.box-title{position:absolute;left:609px;font-size:9.6px;letter-spacing:.8px;color:#222}
.box-text{position:absolute;left:589px;width:130px;font-size:7.4px;line-height:12.8px;color:#777}
.box-link{position:absolute;left:589px;font-size:7.6px;color:var(--green)}
.accordion{position:absolute;left:146px;top:748px;width:406px;border:1px solid var(--rule)}
.accordion .row{height:24.4px;border-top:1px solid var(--rule);display:flex;align-items:center;font-size:7.8px;color:#666;padding-left:7px}
.accordion .row:first-child{border-top:none}
.plus{width:9px;height:9px;border:1px solid #ccc;margin-right:8px;position:relative}
.plus::before{content:"";position:absolute;left:1px;right:1px;top:3.5px;height:1px;background:#ccc}
.plus::after{content:"";position:absolute;top:1px;bottom:1px;left:3.5px;width:1px;background:#ccc}
.portrait{position:absolute;left:589px;top:729px;width:129px;height:110px;background:linear-gradient(160deg,#c9b79b,#e7d3c0 55%,#bdb1a4)}
.quote{position:absolute;left:589px;top:845px;width:130px;font-size:7.6px;line-height:12.8px;color:#777}
.cite{position:absolute;left:589px;top:917px;font-size:7.6px;color:var(--green)}
.cite i{color:#777}
.footer{position:absolute;left:0;top:962px;width:913px;height:196px;background:var(--foot)}
.f-head{position:absolute;top:28px;font-size:8.6px;letter-spacing:.9px;color:#aaa}
.f-text{position:absolute;font-size:7.4px;line-height:12.8px;color:var(--foot-text)}
.f-text b{color:#eee;font-weight:600}
.social{position:absolute;top:94px;display:flex;align-items:center;gap:5px;font-size:6.2px;line-height:7.4px;color:#ddd;font-weight:600}
.social span.sq{width:18px;height:18px;border-radius:2px}
.news{position:absolute;left:337px;display:flex;gap:7px}
.news .thumb{width:21px;height:20px;background:linear-gradient(135deg,#555,#7a6a66);border:1px solid #444}
.news .t{font-size:6.8px;line-height:10.6px;color:#eee;font-weight:600;width:100px}
.news .d{font-size:5.8px;color:#888;font-weight:400;display:block}
.tags{position:absolute;left:503px;top:43px;width:130px;display:flex;flex-wrap:wrap;gap:1px}
.tag{border:1px solid #3e3e3e;font-size:6.2px;color:#ddd;padding:3px 5px}
.cats{position:absolute;left:503px;top:112px;font-size:7.6px;line-height:12.8px;color:#ddd}
.bottom-bar{position:absolute;left:0;top:1158px;width:913px;height:42px;background:var(--foot-bar)}
.copy{position:absolute;left:171px;top:17px;font-size:6.8px;color:#ccc}
.f-nav{position:absolute;top:17px;font-size:6.8px;color:#ccc}
</style>
</head>
<body>

<header class="site-header">
  <div class="brand"><span class="dot"></span>tranquil harbour</div>
  <span class="nav active" style="left:418px">Home</span>
  <span class="nav" style="left:456px">Therapies</span>
  <span class="nav" style="left:509px">Issues</span>
  <span class="nav" style="left:547px">Our Locations</span>
  <span class="nav" style="left:616px">Testimonials</span>
  <span class="nav" style="left:680px">About</span>
  <span class="nav" style="left:719px">Contact</span>
  <svg class="abs" style="left:764px;top:21px" width="10" height="10" viewBox="0 0 10 10"><circle cx="4" cy="4" r="3" fill="none" stroke="#888" stroke-width="1.4"/><line x1="6.2" y1="6.2" x2="9" y2="9" stroke="#888" stroke-width="1.6"/></svg>
  <div class="nav-underline"></div>
</header>

<div class="title-band">
  <span class="page-title">Home</span>
  <span class="crumbs">You are here: &nbsp;Home</span>
</div>

<section class="hero">
  <div class="hero-photo" role="img" aria-label="Two cupped hands sheltering a young green seedling growing from a mound of soil"></div>
  <div class="hero-title">We Care for you</div>
  <div class="hero-sub">This is Pixelcraft's version &nbsp;of Lorem Ipsum.<br>Proin gravida nibh vel velit auctor aliquet.</div>
  <div class="hero-brand"><span class="dot"></span>tranquil harbour</div>
  <svg class="ctrl" style="left:433px" viewBox="0 0 14 14"><circle cx="7" cy="7" r="7" fill="#444"/><path d="M5.5 4.2 L10 7 L5.5 9.8Z" fill="#fff"/></svg>
  <svg class="ctrl" style="left:472px" viewBox="0 0 14 14"><circle cx="7" cy="7" r="7" fill="#aaa"/><rect x="4.6" y="4.3" width="1.6" height="5.4" fill="#fff"/><rect x="7.8" y="4.3" width="1.6" height="5.4" fill="#fff"/></svg>
</section>

<div class="h-rule" style="left:146px;top:508px;width:406px"></div>
<h2 class="section" style="left:146px;top:500px">Welcome to our website</h2>
<p class="body-copy">Aenean sollicitudin, lorem quis bibendum auctor, nisi elit consequat ipsum, nec sagittis sem nibh id elit. Duis sed odio sit amet nibh vulputate cursus a sit amet mauris. Morbi accumsan ipsum velit. Nam nec tellus a odio tincidunt auctor a ornare odio. Sed non &nbsp;mauris vitae erat consequat auctor eu in elit. Class aptent taciti sociosqu ad litora torquent per conubia nostra, per inceptos himenaeos. Mauris in erat justo. Nullam ac urna eu felis dapibus condimentum sit amet a augue. Sed non neque elit. Sed ut imperdiet nisi. Proin condimentum fermentum nunc. Etiam pharetra, erat sed fermentum feugiat, velit mauris egestas quam, ut aliquam massa nisl quis neque. Suspendisse in orci enim.</p>

<svg class="abs" style="left:589px;top:500px" width="11" height="11" viewBox="0 0 24 24"><path d="M6.6 10.8c1.4 2.8 3.8 5.1 6.6 6.6l2.2-2.2c.3-.3.7-.4 1-.2 1.1.4 2.3.6 3.6.6.6 0 1 .4 1 1V20c0 .6-.4 1-1 1C10.6 21 3 13.4 3 4c0-.6.4-1 1-1h3.5c.6 0 1 .4 1 1 0 1.3.2 2.5.6 3.6.1.3 0 .7-.2 1z" fill="#222"/></svg>
<span class="box-title" style="top:500px">CALL US</span>
<p class="box-text" style="top:521px">Proin gravida nibh vel velit auctor aliquet.</p>
<span class="box-link" style="top:554px">1800 454 XXXX</span>

<svg class="abs" style="left:589px;top:586px" width="13" height="9" viewBox="0 0 13 9"><rect width="13" height="9" fill="#222"/><path d="M0 0 L6.5 5 L13 0" fill="none" stroke="#fff" stroke-width="1.2"/></svg>
<span class="box-title" style="top:583px">ICONBOX TITLE</span>
<p class="box-text" style="top:604px">Proin gravida nibh vel velit auctor aliquet.</p>
<span class="box-link" style="top:637px">info@tranquilharbourpsych.com</span>

<div class="h-rule" style="left:146px;top:681px;width:627px"></div>

<div class="h-rule" style="left:146px;top:715px;width:406px"></div>
<h2 class="section" style="left:146px;top:707px">Our Therapy Services include:</h2>
<div class="accordion">
  <div class="row"><span class="plus"></span>Counselling</div>
  <div class="row"><span class="plus"></span>Psychotherapy</div>
  <div class="row"><span class="plus"></span>Cognitive Therapy (CBT)</div>
  <div class="row"><span class="plus"></span>Couples Counselling</div>
</div>

<div class="h-rule" style="left:589px;top:715px;width:129px"></div>
<h2 class="section" style="left:589px;top:707px">Testimonials</h2>
<div class="portrait" role="img" aria-label="Portrait photograph of a smiling client"></div>
<p class="quote">“ Proin gravida nibh vel velit auctor aliquet. Aenean sollicitudin, lorem quis bibendum auctor, nisi elit consequat ipsum, nec sagittis sem nibh id elit. ”</p>
<span class="cite">- Mara, <i>Newyork</i></span>

<footer class="footer">
  <span class="f-head" style="left:171px">INTERESTING LINKS</span>
  <p class="f-text" style="left:171px;top:45px;width:130px">Bellow are some interesting links for you! Enjoy your stay :)</p>
  <div class="social" style="left:171px"><span class="sq" style="background:#3aa7dd"></span>Follow<br>on Chirper</div>
  <div class="social" style="left:235px"><span class="sq" style="background:#f39524"></span>Subscribe<br>to RSS Feed</div>

  <span class="f-head" style="left:337px">LATEST NEWS</span>
  <div class="news" style="top:50px"><span class="thumb"></span><span class="t">Postformat Gallery: Multiple images<span class="d">October 21, 2013 - 3:31 pm</span></span></div>
  <div class="news" style="top:92px"><span class="thumb"></span><span class="t">Snowboarding is fun!<span class="d">December 12, 2012 - 9:11 pm</span></span></div>
  <div class="news" style="top:122px"><span class="thumb"></span><span class="t">This is a standard post format with preview Picture<span class="d">January 14, 2012 - 1:13 pm</span></span></div>

  <span class="f-head" style="left:503px">TAGS</span>
  <div class="tags"><span class="tag">are</span><span class="tag">landscape</span><span class="tag">nice</span><span class="tag">portrait</span><span class="tag">some</span><span class="tag">tags</span><span class="tag">these</span></div>
  <span class="f-head" style="left:503px;top:95px">CATEGORIES</span>
  <p class="cats">Breaking News<br>Frontpage Article<br>Images<br>News</p>

  <span class="f-head" style="left:669px">BUSINESS HOURS</span>
  <p class="f-text" style="left:669px;top:45px;width:135px">Our support Hotline is available 24 Hours a day: (555) 343 456 7891</p>
  <p class="f-text" style="left:669px;top:83px"><b>Monday-Friday:</b> 9am to 5pm<br><b>Saturday:</b> 10am to 2pm<br><b>Sunday:</b> Closed</p>
</footer>

<div class="bottom-bar">
  <span class="copy">© Copyright - Harbourline Theme Demo - Harbourline Theme by Velmar</span>
  <span class="f-nav" style="left:525px">Home</span>
  <span class="f-nav" style="left:557px">Features</span>
  <span class="f-nav" style="left:596px">Headers</span>
  <span class="f-nav" style="left:635px">Portfolio</span>
  <span class="f-nav" style="left:675px">Blog</span>
  <span class="f-nav" style="left:702px">Pages</span>
  <span class="f-nav" style="left:733px">Shortcodes</span>
  <span class="f-nav" style="left:781px">Shop</span>
</div>

</body>
</html>
```